Veterinary TPLO Surgery Flyer Design

Please use this flyer to make a professional-looking 1 page, double-sided client handout regarding TPLO.

You can visit our website at www.brookferrypetcare.com & www.northgroveanimalsurgery.com for additional logo information. The flyer should include all the text from the one provided.

Target Market(s)

Client communication to for referral surgery between sister veterinary clinics

Industry/Entity Type

Veterinary

Requirements
Must have
• The text included
Nice to have
• Nice to have the Willow Crest Avenue Animal CLinic & Dr. Pettigrew Mobile vet logos incorporated.

```html
<!DOCTYPE html>
<html lang="en">
<head>
<meta charset="utf-8">
<title>TPLO Surgery Client Handout</title>
<link href="https://fonts.googleapis.com/css2?family=Poppins:wght@400;500;600;700&family=Saira+Semi+Condensed:wght@600;700&display=swap" rel="stylesheet">
<style>
:root{
  --green:#466b3c;
  --olive:#7a9a50;
  --orange:#f7962f;
  --ink:#1c1c1c;
  --body:#2b2b2b;
  --white:#ffffff;
  --grey:#e6e6e6;
}
*{margin:0;padding:0;box-sizing:border-box}
html,body{width:1200px;height:964px;overflow:hidden;background:var(--white)}
.flyer{position:relative;width:1200px;height:964px;overflow:hidden;font-family:"Poppins",sans-serif;color:var(--body)}
.abs{position:absolute}
.display{font-family:"Saira Semi Condensed",sans-serif;font-weight:700;color:var(--ink);letter-spacing:.1px}
.shape{position:absolute;top:0;left:0}
.photo{position:absolute}
.brand{left:26px;top:40px;display:flex;align-items:center;gap:8px}
.brand .dot{width:14px;height:14px;border-radius:50%;background:var(--green)}
.brand span{font-weight:700;font-size:15px;color:var(--green)}
.hero-title{left:24px;top:162px;font-size:35px;line-height:46px;color:var(--white);white-space:nowrap}
.hero-rule{left:27px;top:261px;width:145px;height:2px;background:var(--olive)}
.hero-by{left:26px;top:284px;font-size:12px;font-weight:500;color:var(--white);white-space:nowrap}
.hero-by b{color:var(--orange);font-size:15px;font-weight:600}
.hero-sub{left:26px;top:308px;font-size:12px;font-weight:500;color:var(--white);white-space:nowrap}
.col{display:flex;flex-direction:column}
.h2{font-size:17px;line-height:21px}
.rule{width:44px;height:3px;background:var(--orange);margin:6px 0 10px}
.txt{font-size:9.6px;line-height:15.2px}
.txt strong{font-weight:700;color:var(--ink)}
.gap{height:12px}
.benefit{margin-bottom:10px}
.benefit h3{font-size:11px;font-weight:500;color:var(--ink);display:flex;align-items:center;gap:5px}
.benefit p{font-size:9.6px;line-height:15.2px;margin-top:1px}
.paw{width:12px;height:10px}
.steps{width:470px}
.steps p{font-size:9.6px;line-height:17px;margin-bottom:2px}
.steps .n{font-family:"Saira Semi Condensed",sans-serif;font-weight:700;color:var(--orange);font-size:11.5px}
.steps .k{font-family:"Saira Semi Condensed",sans-serif;font-weight:700;color:var(--ink);font-size:11.5px}
.wk{font-family:"Saira Semi Condensed",sans-serif;font-weight:700;color:var(--ink);font-size:10.5px}
.foot-name{font-size:15px;line-height:19px;color:var(--white);font-weight:600;white-space:nowrap}
.foot-phone{font-size:21px;color:var(--white);display:flex;align-items:center;gap:10px;font-weight:600;white-space:nowrap}
.foot-link{font-family:"Saira Semi Condensed",sans-serif;font-weight:600;font-size:10.5px;display:flex;align-items:center;gap:6px;white-space:nowrap}
.ico{width:11px;height:11px;flex:none}
.clinic-foot{left:760px;top:874px;display:flex;gap:12px;align-items:stretch}
.clinic-foot .name{font-size:13.5px}
.divider{width:1px;background:var(--olive)}
.links{display:flex;flex-direction:column;gap:14px;padding-top:4px}
</style>
</head>
<body>
<div class="flyer">

  <svg class="shape" width="1200" height="964" viewBox="0 0 1200 964" aria-hidden="true">
    <polygon points="268,0 330,0 272,97 222,97" fill="var(--grey)"/>
    <polygon points="355,0 600,0 600,60 360,60 318,130 304,102" fill="var(--orange)"/>
    <polygon points="0,123 262,123 405,380 0,380" fill="var(--green)"/>
    <polygon points="0,380 380,380 388,390 0,390" fill="var(--orange)"/>
    <polygon points="0,850 250,850 256,857 0,857" fill="var(--orange)"/>
    <polygon points="0,857 278,857 350,964 0,964" fill="var(--green)"/>
    <polygon points="315,911 600,911 600,964 350,964" fill="var(--orange)"/>
    <polygon points="600,797 730,964 600,964" fill="var(--orange)"/>
    <polygon points="712,858 1200,858 1200,964 792,964" fill="var(--green)"/>
    <polygon points="648,845 678,828 792,964 760,964" fill="var(--olive)"/>
  </svg>

  <div class="photo" role="img" aria-label="Photo of a smiling veterinarian in blue scrubs holding a golden dog"
       style="left:300px;top:72px;width:300px;height:308px;background:linear-gradient(135deg,#e9edf0,#c49259 55%,#3c6b9c);clip-path:polygon(38px 0,300px 0,300px 308px,118px 308px,0 102px,10px 22px)"></div>
  <div class="photo" role="img" aria-label="Photo of a veterinarian examining a reddish-brown long-haired dog on an exam table"
       style="left:600px;top:0;width:600px;height:229px;background:linear-gradient(180deg,#dde3e8,#e9ecef 45%,#b5652e 75%,#f1f1f1)"></div>

  <div class="abs brand"><div class="dot"></div><span>Helena Pettigrew</span></div>

  <h1 class="abs display hero-title">Advanced<br>Orthopedic Care</h1>
  <div class="abs hero-rule"></div>
  <p class="abs hero-by">by <b>Dr. Helena Pettigrew</b>, DVM, DNCVS-sa</p>
  <p class="abs hero-sub">TPLO Surgery at Willow Crest Avenue Animal Clinic</p>

  <section class="abs col" style="left:23px;top:410px;width:264px">
    <h2 class="display h2">About Dr. Helena Pettigrew</h2>
    <div class="rule"></div>
    <p class="txt">Dr. Helena Pettigrew is a board-certified veterinary surgeon (Diplomate of the National College of Veterinary Surgeons) with over 18 years of experience in small animal surgery. A graduate of Great Lakes State University, she completed her surgical residency at Harborview School of Veterinary Medicine. Through her mobile practice, Roving Surgical Partners, Dr. Pettigrew now provides advanced surgical procedures—such as TPLO—directly at local clinics.</p>
    <div style="height:24px"></div>
    <h2 class="display h2">Why Choose Willow Crest Avenue Animal Clinic?</h2>
    <div class="rule"></div>
    <p class="txt">Partnering with Dr. Pettigrew, Willow Crest Avenue Animal Clinic offers advanced orthopedic surgery on-site—eliminating the need for referrals or travel. This collaboration ensures your pet receives expert surgical care in a familiar, trusted environment.</p>
    <div style="height:8px"></div>
    <p class="txt">Our clinic works directly with your primary veterinarian to share medical records, diagnostics, and prescriptions, ensuring seamless and coordinated care for your pet.</p>
  </section>

  <section class="abs col" style="left:322px;top:408px;width:272px">
    <h2 class="display h2">What is TPLO Surgery?</h2>
    <div class="rule"></div>
    <p class="txt"><strong>Tibial Plateau Leveling Osteotomy (TPLO)</strong> is a surgical procedure that stabilizes the stifle (knee) joint following a <strong>cranial cruciate ligament (CCL)</strong> rupture—a common orthopedic injury in dogs. The procedure involves altering the angle of the tibial plateau to eliminate abnormal joint motion, restoring stability and improving function.</p>
  </section>
  <div class="photo" role="img" aria-label="Illustration of a knee joint before and after tibial plateau leveling"
       style="left:322px;top:571px;width:126px;height:98px;border-radius:8px;background:linear-gradient(135deg,#ececec,#d8d2c0)"></div>
  <div class="photo" role="img" aria-label="X-ray images of a dog's stifle with a TPLO plate"
       style="left:470px;top:571px;width:126px;height:98px;border-radius:8px;background:linear-gradient(135deg,#1a1a1a,#6f7270 50%,#121212)"></div>

  <section class="abs col" style="left:321px;top:690px;width:275px">
    <h2 class="display h2">Benefits of TPLO Surgery</h2>
    <div class="rule"></div>
    <div class="benefit">
      <h3><svg class="paw" viewBox="0 0 12 10"><g fill="var(--olive)"><circle cx="2" cy="4" r="1.5"/><circle cx="4.5" cy="1.6" r="1.5"/><circle cx="7.5" cy="1.6" r="1.5"/><circle cx="10" cy="4" r="1.5"/><ellipse cx="6" cy="7.3" rx="2.8" ry="2.3"/></g></svg>Enhanced Joint Stability</h3>
      <p>Restores natural biomechanics, reducing pain and improving mobility.</p>
    </div>
    <div class="benefit">
      <h3><svg class="paw" viewBox="0 0 12 10"><g fill="var(--olive)"><circle cx="2" cy="4" r="1.5"/><circle cx="4.5" cy="1.6" r="1.5"/><circle cx="7.5" cy="1.6" r="1.5"/><circle cx="10" cy="4" r="1.5"/><ellipse cx="6" cy="7.3" rx="2.8" ry="2.3"/></g></svg>Faster Recovery</h3>
      <p>Restores natural biomechanics, reducing pain and improving mobility.</p>
    </div>
    <div class="benefit">
      <h3><svg class="paw" viewBox="0 0 12 10"><g fill="var(--olive)"><circle cx="2" cy="4" r="1.5"/><circle cx="4.5" cy="1.6" r="1.5"/><circle cx="7.5" cy="1.6" r="1.5"/><circle cx="10" cy="4" r="1.5"/><ellipse cx="6" cy="7.3" rx="2.8" ry="2.3"/></g></svg>Proven Long-Term Success</h3>
      <p>TPLO is particularly effective in large and active breeds.</p>
    </div>
  </section>

  <section class="abs col" style="left:633px;top:244px;width:556px">
    <h2 class="display h2">Diagnostic Radiographs vs. TPLO Planning Radiographs</h2>
    <div class="rule"></div>
    <p class="txt">While diagnostic radiographs may confirm a CCL tear, <strong>they are not sufficient for surgical planning</strong>. TPLO requires <strong>three advanced technique</strong> radiographic views with precise measurements, which must be performed under sedation to reduce discomfort and allow accurate positioning.</p>
    <div class="gap"></div>
    <h2 class="display h2">Expected Process</h2>
    <div class="rule"></div>
    <div class="steps">
      <p><span class="n">01.</span> <span class="k">Diagnosis:</span> Your pet is diagnosed with stifle instability (CCL tear) by your veterinarian.</p>
      <p><span class="n">02.</span> <span class="k">Referral:</span> Your veterinarian contacts the surgical coordinator at Willow Crest Avenue Animal Clinic.</p>
      <p><span class="n">03.</span> <span class="k">Consultation</span>: The coordinator contacts you to schedule a 1-hour consultation to review the procedure, estimated costs, and available surgery dates.</p>
      <p><span class="n">04.</span> <span class="k">Planning Radiographs</span>: These specialized X-rays are typically taken during the consultation under light sedation.</p>
      <p><span class="n">05.</span> <span class="k">Surgical Review:</span> Dr. Pettigrew reviews the radiographs and your pet’s medical history to confirm candidacy for TPLO.</p>
      <p><span class="n">06.</span> <span class="k">Deposit:</span> A $3,500 deposit secures Dr. Pettigrew’s travel and surgery date. This is refundable if canceled at least 5 days prior to the scheduled procedure.</p>
      <p><span class="n">07.</span> <span class="k">Surgery Day:</span> Your pet is dropped off in the morning and surgery is performed the same day.</p>
      <p>08. Discharge: You’ll receive a post-surgery update and your pet will go home that evening.</p>
    </div>
    <div style="height:8px"></div>
    <h2 class="display h2">Post-Operative Care &amp; Follow-Up</h2>
    <div class="rule"></div>
    <p class="txt" style="font-weight:600;color:var(--ink)">Two follow-up appointments will be scheduled:</p>
    <p class="txt" style="margin-top:6px"><span class="wk">4 Weeks Post-Op:</span> Evaluate healing, refill medications, and address any questions.<br><span class="wk">8 Weeks Post-Op:</span> Sedated radiographs will confirm proper healing of the surgical site and tibia.</p>
    <p class="txt" style="margin-top:14px">Dr. Pettigrew will stay in direct contact with you during your pet’s recovery using her custom mobile app, which allows for secure messaging and provides detailed post-operative instructions</p>
  </section>

  <p class="abs display foot-name" style="left:24px;top:876px">Roving Surgical Partners<br>(Dr. Helena Pettigrew)</p>
  <div class="abs display foot-phone" style="left:28px;top:920px">
    <svg width="20" height="20" viewBox="0 0 24 24" fill="none" stroke="var(--white)" stroke-width="1.6"><path d="M5 3h4l2 5-2.5 1.5a11 11 0 0 0 6 6L16 13l5 2v4a2 2 0 0 1-2 2A16 16 0 0 1 3 5a2 2 0 0 1 2-2z"/></svg>
    (810) 555-0142
  </div>
  <div class="abs foot-link" style="left:366px;top:923px;color:var(--ink)">
    <svg class="ico" viewBox="0 0 12 10"><rect x=".5" y=".5" width="11" height="9" fill="var(--ink)"/><path d="M1 1l5 4 5-4" stroke="var(--white)" fill="none"/></svg>drpettigrew@rovingsurgical.com</div>
  <div class="abs foot-link" style="left:366px;top:940px;color:var(--ink)">
    <svg class="ico" viewBox="0 0 12 12"><circle cx="6" cy="6" r="5.5" fill="var(--ink)"/><path d="M.5 6h11M6 .5v11" stroke="var(--orange)" stroke-width=".8"/></svg>www.northgroveanimalsurgery.com</div>

  <div class="abs clinic-foot">
    <div>
      <p class="display foot-name name">Willow Crest Avenue Animal Clinic</p>
      <div class="display foot-phone" style="margin-top:8px">
        <svg width="20" height="20" viewBox="0 0 24 24" fill="none" stroke="var(--white)" stroke-width="1.6"><path d="M5 3h4l2 5-2.5 1.5a11 11 0 0 0 6 6L16 13l5 2v4a2 2 0 0 1-2 2A16 16 0 0 1 3 5a2 2 0 0 1 2-2z"/></svg>
        (517) 555-0187
      </div>
    </div>
    <div class="divider"></div>
    <div class="links">
      <div class="foot-link" style="color:var(--white)">
        <svg class="ico" viewBox="0 0 12 10"><rect x=".5" y=".5" width="11" height="9" fill="var(--white)"/><path d="M1 1l5 4 5-4" stroke="var(--green)" fill="none"/></svg>info@brookferrypetcare.com</div>
      <div class="foot-link" style="color:var(--white)">
        <svg class="ico" viewBox="0 0 12 12"><circle cx="6" cy="6" r="5.5" fill="var(--white)"/><path d="M.5 6h11M6 .5v11" stroke="var(--green)" stroke-width=".8"/></svg>www.brookferrypetcare.com</div>
    </div>
  </div>

</div>
</body>
</html>
```